TV+Music+Social Network+Entertainment+yellowpages= Designers lol

TV+ Music+ Social Network +Entertainment+ yellowpages=

ZAVQUEL.COM

Zavquel is a one-stop shop promotional plateform that will communicate information to all user of what is COOL, NEW and Exicting in your Neighborhood.(News,Events,Entertainment,ect) We promote for all User/Entrepreneur/business/Talents.We are the future and dream destination for all to whom owns a computer. Forming the the World Wide Web into your Local Wide Web. (Atlanta, Dallas, Las Vegas, New York ect.)

* EX: ( WWW. ??? .com =LWW. ??? .com)
WORLD = LOCAL

* Goal/Mission: Have customer/user visit the website and then leave their house to go experience life in their respective surroundings.

/////////////////////////Web page///////////////////////

Colors:Blue/Green/black

include: interchangable background picture @ top (to update easily and keep fresh) On this background picture include logo (top left) login/sign (top left)

Major Tabs: Music/Daylife/Nightlife/Video/Shop

• Tv screen/search engine

```html
<!DOCTYPE html>
<html lang="en">
<head>
<meta charset="utf-8">
<title>Zavquel</title>
<link href="https://fonts.googleapis.com/css2?family=Source+Sans+3:wght@400;600&display=swap" rel="stylesheet">
<style>
  :root{
    --page-bg:#000;
    --text-light:#ffffff;
    --text-dark:#222;
    --accent-blue:#1a9ad6;
    --field-bg:#e3e4e6;
    --field-border:#c4c6c9;
    --frame-dark:#141414;
    --frame-edge:#3a3a3a;
    --silver:#c9cbcd;
    --silver-dark:#8d9094;
    --dash:#8f8f8f;
    --footer-dash:#2c2c2c;
  }
  *{margin:0;padding:0;box-sizing:border-box}
  html,body{width:1200px;height:800px;overflow:hidden;background:var(--page-bg)}
  body{font-family:"Source Sans 3",Arial,sans-serif;color:var(--text-light);position:relative}
  .abs{position:absolute}

  .brand{left:212px;top:38px;display:flex;align-items:center;gap:12px}
  .brand-dot{width:50px;height:50px;border-radius:50%;background:var(--accent-blue)}
  .brand-name{font-size:38px;font-weight:600;color:var(--text-light);letter-spacing:.5px}

  .main-nav{top:71px;left:727px;display:flex;gap:0;font-size:13px}
  .main-nav a{color:var(--text-light);text-decoration:none;position:absolute;white-space:nowrap}

  .tv-frame{left:211px;top:123px;width:782px;height:481px;background:var(--frame-dark);border:1px solid var(--frame-edge);border-radius:3px}
  .tv-maker{left:246px;top:142px;font-size:8px;letter-spacing:1px;color:#bbb;font-weight:600}
  .tv-band{left:211px;top:604px;width:782px;height:29px;background:linear-gradient(#e4e5e6,var(--silver) 50%,var(--silver-dark));border-radius:0 0 3px 3px}
  .tv-neck{left:575px;top:592px;width:50px;height:41px;background:linear-gradient(90deg,#777,#ddd,#777)}
  .tv-base{left:402px;top:633px;width:407px;height:37px;background:linear-gradient(#1a1a1a,#3a3a3a 70%,#aaa);border-radius:4px 4px 10px 10px}

  .screen{left:252px;top:158px;width:705px;height:393px;background:#fff}
  .section-title{color:var(--accent-blue);font-size:17px;font-weight:400}
  .video-title{left:29px;top:22px}
  .news-title{left:371px;top:22px}

  .player{left:29px;top:51px;width:305px;height:185px;background:#000}
  .thumb{left:46px;top:20px;width:212px;height:130px;background:linear-gradient(#9a8474,#7d6a5e)}
  .controls{left:0;bottom:0;width:305px;height:17px;background:#1b1b1b}
  .progress{left:0;top:0;width:305px;height:3px;background:#555}
  .progress-fill{left:0;top:0;width:74px;height:3px;background:#d11}
  .time{left:40px;top:5px;font-size:6px;color:#ccc}

  .dash-news{left:373px;top:53px;width:310px;border-top:1px dashed var(--dash)}
  .news-list{left:388px;top:73px;width:290px;list-style:none}
  .news-list li{position:relative;padding-left:23px;font-size:11px;line-height:15.5px;color:var(--text-dark);height:62px}
  .news-list svg{position:absolute;left:0;top:2px}

  .dash-mid{left:29px;top:259px;width:656px;border-top:1px dashed var(--dash)}
  .contact-title{left:42px;top:300px}
  .field{background:var(--field-bg);border:1px solid var(--field-border);font-size:11px;color:var(--text-dark);padding:5px 9px}
  .f-name{left:182px;top:273px;width:180px;height:26px}
  .f-email{left:182px;top:308px;width:180px;height:26px}
  .f-phone{left:182px;top:346px;width:180px;height:26px}
  .f-message{left:370px;top:273px;width:222px;height:100px}
  .submit{left:606px;top:305px;width:76px;height:29px;background:var(--accent-blue);color:#fff;font-size:17px;display:flex;align-items:center;justify-content:center}

  .footer-line{left:214px;top:706px;width:782px;border-top:1px dashed var(--footer-dash)}
  .copyright{left:221px;top:736px;font-size:12px}
  .follow{left:836px;top:738px;font-size:12px}
  .social{top:738px;width:15px;height:15px;border-radius:2px}
  .s1{left:906px;background:#3b5a9a}
  .s2{left:938px;background:#4fb3e8}
  .s3{left:965px;background:#3c6fb0}
  .s4{left:988px;background:#ee7b1e}
</style>
</head>
<body>
  <header>
    <div class="abs brand"><span class="brand-dot"></span><span class="brand-name">Zavquel</span></div>
    <nav class="abs main-nav">
      <a style="left:0">Music</a>
      <a style="left:56px">Daylife</a>
      <a style="left:118px">Nightlife</a>
      <a style="left:184px">Video</a>
      <a style="left:235px">Shop</a>
    </nav>
  </header>

  <div class="abs tv-frame"></div>
  <div class="abs tv-maker">NORVELL</div>
  <div class="abs tv-neck"></div>
  <div class="abs tv-band"></div>
  <div class="abs tv-base"></div>

  <main class="abs screen">
    <h2 class="abs section-title video-title">VIDEO</h2>
    <div class="abs player">
      <div class="abs thumb" role="img" aria-label="Video still: people seen from above forming letters on the ground"></div>
      <div class="abs controls">
        <div class="abs progress"></div>
        <div class="abs progress-fill"></div>
        <svg class="abs" style="left:10px;top:6px" width="8" height="8"><path d="M1 0L7 4L1 8Z" fill="#ccc"/></svg>
        <span class="abs time">0:53 / 3:48</span>
      </div>
    </div>

    <h2 class="abs section-title news-title">News</h2>
    <div class="abs dash-news"></div>
    <ul class="abs news-list">
      <li><svg width="13" height="13"><rect x=".5" y=".5" width="12" height="12" fill="#eee" stroke="#999"/><path d="M3 4h7M3 6.5h7M3 9h7" stroke="#999"/></svg>It is a long established fact that a reader will be distracted by the readable content of a page when looking at its layout</li>
      <li><svg width="13" height="13"><rect x=".5" y=".5" width="12" height="12" fill="#eee" stroke="#999"/><path d="M3 4h7M3 6.5h7M3 9h7" stroke="#999"/></svg>It is a long established fact that a reader will be distracted by the readable content of a page when looking at its layout</li>
      <li><svg width="13" height="13"><rect x=".5" y=".5" width="12" height="12" fill="#eee" stroke="#999"/><path d="M3 4h7M3 6.5h7M3 9h7" stroke="#999"/></svg>It is a long established fact that a reader will be distracted by the readable content of a page when looking at its layout</li>
    </ul>

    <div class="abs dash-mid"></div>
    <h2 class="abs section-title contact-title">Quick Contact</h2>
    <div class="abs field f-name">Name</div>
    <div class="abs field f-email">E mail</div>
    <div class="abs field f-phone">Phone</div>
    <div class="abs field f-message">Message</div>
    <div class="abs submit">Submit</div>
  </main>

  <footer>
    <div class="abs footer-line"></div>
    <p class="abs copyright">Copyrights @ 2012 All Rights Reserved</p>
    <p class="abs follow">Follow Us</p>
    <span class="abs social s1"></span>
    <span class="abs social s2"></span>
    <span class="abs social s3"></span>
    <span class="abs social s4"></span>
  </footer>
</body>
</html>
```